Brenwick Realty
Business cards and stationery
Brenwick Realty - Real Estate
Creative Brief
Modern
Marian Talcott
Director
Level 4 218 Garnet Lane Melbourne VIC 3000
marian@brenwickrealty-example.com.au
www.brenwickrealty-example.com.au
Brenwick Summit Realty 518902K Licensee Marian Talcott
Stationery needs to have the licensee info on the bottom of letterhead
black background logo in centre

```html
<!DOCTYPE html>
<html lang="en">
<head>
<meta charset="utf-8">
<title>Brenwick Realty – Business Cards</title>
<link rel="stylesheet" href="https://fonts.googleapis.com/css2?family=Open+Sans:wght@400;600;700&display=swap">
<style>
  :root {
    --bg: #d9d9db;
    --card-black: #0b0b0c;
    --pink: #e0157f;
    --pink-deep: #b80d66;
    --blue: #2aa6e0;
    --white: #ffffff;
    --grey-text: #c9c9cc;
  }
  * { margin: 0; padding: 0; box-sizing: border-box; }
  html, body { width: 1200px; height: 646px; overflow: hidden; }
  body {
    background: var(--bg);
    font-family: "Open Sans", Arial, sans-serif;
    position: relative;
  }
  .card {
    position: absolute;
    top: 158px;
    width: 540px;
    height: 330px;
    background: var(--card-black);
    border-radius: 4px;
    overflow: hidden;
    box-shadow: 0 6px 18px rgba(0,0,0,0.25);
  }
  .card--back { left: 40px; }
  .card--front { left: 620px; }

  .brand-name {
    font-weight: 700;
    color: var(--pink);
    white-space: nowrap;
    display: flex;
    align-items: center;
    gap: 10px;
  }
  .brand-dot {
    width: 14px; height: 14px;
    border-radius: 50%;
    background: var(--pink);
    flex: none;
  }

  /* back side */
  .back-logo {
    position: absolute;
    left: 0; right: 0; top: 112px;
    justify-content: center;
    font-size: 38px;
  }
  .back-website {
    position: absolute;
    left: 0; right: 0; top: 182px;
    text-align: center;
    color: var(--white);
    font-size: 12px;
    font-weight: 600;
    letter-spacing: 1.5px;
  }
  .back-licence {
    position: absolute;
    left: 0; right: 0; bottom: 22px;
    text-align: center;
    color: var(--grey-text);
    font-size: 8.5px;
    letter-spacing: 0.4px;
  }

  /* front side */
  .front-shapes { position: absolute; inset: 0; }
  .front-person {
    position: absolute;
    right: 26px; top: 24px;
    text-align: right;
  }
  .person-name { color: var(--white); font-size: 15px; font-weight: 700; }
  .person-role { color: var(--grey-text); font-size: 10px; margin-top: 2px; }
  .front-logo {
    position: absolute;
    left: 34px; top: 138px;
    font-size: 27px;
  }
  .contact-list {
    position: absolute;
    right: 26px; top: 84px;
    list-style: none;
    color: var(--white);
    font-size: 10px;
    line-height: 1.45;
    text-align: right;
  }
  .contact-address { margin-bottom: 8px; }
  .contact-item {
    display: flex;
    justify-content: flex-end;
    align-items: center;
    gap: 6px;
  }
  .contact-icon { width: 10px; height: 10px; flex: none; fill: var(--white); }
</style>
</head>
<body>

  <section class="card card--back" aria-label="Business card back">
    <div class="brand-name back-logo"><span class="brand-dot"></span>Brenwick Realty</div>
    <p class="back-website">www.brenwickrealty-example.com.au</p>
    <p class="back-licence">Licence · Brenwick Summit Realty 518902K · Licensee Marian Talcott</p>
  </section>

  <section class="card card--front" aria-label="Business card front">
    <svg class="front-shapes" viewBox="0 0 540 330" width="540" height="330" aria-hidden="true">
      <path d="M0 262 C 160 312 340 262 540 162 L540 330 L0 330 Z" fill="var(--pink)"/>
      <path d="M0 292 C 160 330 360 300 540 220 L540 330 L0 330 Z" fill="var(--pink-deep)" opacity="0.55"/>
      <path d="M0 246 C 160 296 340 246 540 146" fill="none" stroke="var(--blue)" stroke-width="7"/>
      <path d="M300 0 C 420 28 500 70 540 112" fill="none" stroke="var(--blue)" stroke-width="5"/>
      <path d="M330 0 C 440 22 510 52 540 80" fill="none" stroke="var(--pink)" stroke-width="3"/>
    </svg>

    <div class="front-person">
      <p class="person-name">Marian Talcott</p>
      <p class="person-role">Director</p>
    </div>

    <div class="brand-name front-logo"><span class="brand-dot"></span>Brenwick Realty</div>

    <ul class="contact-list">
      <li class="contact-address">Level 4<br>218 Garnet Lane<br>Melbourne VIC 3000</li>
      <li class="contact-item">(03) 9555 0142
        <svg class="contact-icon" viewBox="0 0 10 10"><path d="M2 0.5 L3.6 0.5 L4.3 2.8 L3.2 3.7 C3.8 5 5 6.2 6.3 6.8 L7.2 5.7 L9.5 6.4 L9.5 8 C9.5 9 8.8 9.5 8 9.5 C4 9.2 0.8 6 0.5 2 C0.5 1.2 1 0.5 2 0.5 Z"/></svg>
      </li>
      <li class="contact-item">0491 570 318
        <svg class="contact-icon" viewBox="0 0 10 10"><rect x="2.5" y="0.5" width="5" height="9" rx="1"/></svg>
      </li>
      <li class="contact-item">(03) 9555 0177
        <svg class="contact-icon" viewBox="0 0 10 10"><rect x="1" y="3" width="8" height="5" rx="0.8"/><rect x="2.5" y="0.8" width="5" height="2.6"/></svg>
      </li>
      <li class="contact-item">marian@brenwickrealty-example.com.au
        <svg class="contact-icon" viewBox="0 0 10 10"><path d="M0.5 2 L9.5 2 L9.5 8 L0.5 8 Z M1 2.5 L5 5.5 L9 2.5" fill="none" stroke="var(--white)" stroke-width="0.9"/></svg>
      </li>
    </ul>
  </section>

</body>
</html>
```